Sports Hatchback Wrap - Attract Attention

Please design a wrap with logos for a company car - 2020 Marlo Vesta Sport Touring Hatchback, images attached.

We would like the design to attract attention and turn heads - perhaps something sporty, like racing stripes. We would also like to have some text - content - as opposed to just graphics and logo everywhere.

Vehicle is the Marlo Vesta Harchback Sport Touring

Please use exact hex code colors of 3f9ed7 and 595959

Logo text font is the Aristocrat font

The remaining area where there is no graphics or font will be clear, to showcase the white diamond sparking paint beneath. We would like the car to remain more than 50% white (paint underneath) showing.

Also would like to see 2 blue racing stripes going down car hood and roof front to back on entite vehicle as part of the design...as one option. And if no racing stripes...inlike a full color front hood with a white logo as another option...like a PELTROD. I like blue accent pieces like small ones in the grill.

Also would like it to be not so busy....a bit more on the simplistic side but still eye catching.

Also no plain text on windows. Color skin is ok on windows but plain text on windows looks tacky. Prefer text on back bumper or harfhback door of car and design on sides of car.

Also like full main logo on front doors of car on both sides

Target Market(s)

Engineering and Architecture Companies

Industry/Entity Type

Engineering Consultant

Font styles to use
Serif
Other font styles liked:
• fonts MUST match the logo

Colors
33a6d7

Requirements
Must have
• There needs to be text in some visible parts of the car - perhaps the sides or the back. It should say:
"Drafting • Staffing • Training"
"kelumplans.example"
"555-014-2276"
And the Chatterpage, Pixelgram, Quipster and WorkLoop logos
Nice to have
• I would like to incorporate sporty graphics into the design - perhaps racing strips, or bright blue trim around the car. We would also like to have the logo (or parts of the logo) visible from every angle - on the hood, roof, sides. The logo can be just the head, the head and text (KEL Drafting), or just the text - feel free to put pieces wherever they will fit.

Less is more - a cleaner minimalistic design will bring more attention to the logo.
Should not have
• No colors other than blue, grey, black, and white - the colors of the logo.

```html
<!DOCTYPE html>
<html lang="en">
<head>
<meta charset="utf-8">
<title>KEL Drafting – Vehicle Wrap, Right Side</title>
<link rel="stylesheet" href="https://fonts.googleapis.com/css2?family=Exo+2:ital,wght@0,400;1,800&family=Tinos&display=swap">
<style>
  :root {
    --brand-blue: #3f9ed7;
    --brand-grey: #595959;
    --ink-dark: #1e1f21;
    --icon-dark: #333538;
    --tab-grey: #4a4e53;
    --paint-white: #ffffff;
  }
  html, body {
    margin: 0;
    padding: 0;
    width: 1200px;
    height: 800px;
    overflow: hidden;
    background: var(--paint-white);
  }
  .wrap-panel {
    display: block;
    width: 1200px;
    height: 800px;
  }
  .accent-band { fill: var(--brand-blue); }
  .lower-panel { fill: var(--ink-dark); }
  .web-address {
    font-family: "Exo 2", sans-serif;
    font-weight: 800;
    font-style: italic;
    font-size: 44px;
    fill: var(--brand-grey);
  }
  .social-dot { fill: var(--icon-dark); }
  .social-name {
    font-family: "Exo 2", sans-serif;
    font-weight: 400;
    font-size: 13px;
    fill: var(--icon-dark);
  }
  .logo-frame {
    fill: none;
    stroke: var(--brand-grey);
    stroke-width: 3;
  }
  .logo-name {
    font-family: "Exo 2", sans-serif;
    font-weight: 400;
    fill: var(--brand-blue);
  }
  .services, .phone {
    font-family: "Exo 2", sans-serif;
    font-weight: 800;
    font-style: italic;
    fill: var(--brand-blue);
  }
  .services { font-size: 42px; }
  .phone { font-size: 34px; }
  .side-tab { fill: var(--tab-grey); }
  .side-tab-label {
    font-family: "Tinos", serif;
    font-size: 24px;
    fill: var(--paint-white);
  }
</style>
</head>
<body>
<svg class="wrap-panel" viewBox="0 0 1200 800" xmlns="http://www.w3.org/2000/svg">
  <defs>
    <linearGradient id="streak-fill" x1="0" y1="0" x2="1" y2="0">
      <stop offset="0" stop-color="#2a7fb3" stop-opacity="0.9"/>
      <stop offset="0.6" stop-color="#3f9ed7" stop-opacity="0.55"/>
      <stop offset="1" stop-color="#3f9ed7" stop-opacity="0"/>
    </linearGradient>
    <linearGradient id="head-fill" x1="0" y1="0" x2="1" y2="0">
      <stop offset="0" stop-color="#3f9ed7"/>
      <stop offset="1" stop-color="#595959" stop-opacity="0.3"/>
    </linearGradient>
  </defs>

  <!-- top accent band with web address -->
  <polygon class="accent-band" points="356,0 598,0 1200,199 1200,292"/>
  <text class="web-address" x="904" y="150" text-anchor="middle" transform="rotate(19 904 135)">kelumplans.example</text>

  <!-- social network names -->
  <g class="social-row" transform="rotate(17 1020 60)">
    <circle class="social-dot" cx="862" cy="56" r="6"/>
    <text class="social-name" x="872" y="61">Chatterpage</text>
    <circle class="social-dot" cx="952" cy="56" r="6"/>
    <text class="social-name" x="962" y="61">Pixelgram</text>
    <circle class="social-dot" cx="1034" cy="56" r="6"/>
    <text class="social-name" x="1044" y="61">Quipster</text>
    <circle class="social-dot" cx="1110" cy="56" r="6"/>
    <text class="social-name" x="1120" y="61">WorkLoop</text>
  </g>

  <!-- logo block -->
  <rect class="head-graphic" x="406" y="121" width="180" height="158" rx="6" fill="url(#head-fill)" role="img" aria-label="Blue circuit-style head emblem with streaking lines"/>
  <rect class="logo-frame" x="548" y="199" width="384" height="285" transform="rotate(-3 740 341)"/>
  <text class="logo-name" x="740" y="372" text-anchor="middle" font-size="150">KEL</text>
  <text class="logo-name" x="705" y="440" text-anchor="middle" font-size="40">Drafting</text>

  <!-- lower dark panel -->
  <polygon class="lower-panel" points="0,285 1200,700 1200,800 0,800"/>
  <polygon class="streak-graphic" points="0,470 880,640 880,800 0,800" fill="url(#streak-fill)" role="img" aria-label="Blue light streak graphic"/>

  <text class="services" x="570" y="540" text-anchor="middle" transform="rotate(20 570 527)">Drafting • Staffing • Training</text>
  <text class="phone" x="626" y="652" text-anchor="middle" transform="rotate(20 626 640)">555-014-2276</text>

  <!-- side indicator tab -->
  <rect class="side-tab" x="1136" y="416" width="64" height="179"/>
  <text class="side-tab-label" x="1168" y="505" text-anchor="middle" dominant-baseline="middle" transform="rotate(90 1168 505)">Right Side</text>
</svg>
</body>
</html>
```